Redesign of existing business card

I would like the "signage" attachment converted into a business card. This needs to be double sided aswell, keeping the phone number and names on the front, and the email + website on the back.

Second attachment is the current business card design.

Larger font for contact details is required.

Must keep to original color themes (electric blue, silver/grey etc)

Back of the card to have blue background with white writing.

Industry/Entity Type

Business

Contact Information for Business Card

Refer to existing design from attachments

Requirements
Must have
• Refer to existing design from attachments
Nice to have

```html
<!DOCTYPE html>
<html lang="en">
<head>
<meta charset="utf-8">
<title>Korvan Electro Services – Business Card</title>
<link href="https://fonts.googleapis.com/css2?family=Exo+2:wght@600;700;800&display=swap" rel="stylesheet">
<style>
  :root {
    --electric-blue: #3f5fc8;
    --deep-blue: #2f49b0;
    --silver-light: #f3f3f4;
    --silver-mid: #dcdcde;
    --silver-dark: #a9a9ad;
    --grey-text: #8a8a8e;
    --backdrop: #2a2a2c;
    --white: #ffffff;
  }
  * { margin: 0; padding: 0; box-sizing: border-box; }
  html, body { width: 1200px; height: 900px; overflow: hidden; }
  body {
    background: var(--backdrop);
    font-family: "Exo 2", Arial, sans-serif;
    position: relative;
  }
  .card {
    position: absolute;
    width: 560px;
    height: 340px;
    border-radius: 22px;
    overflow: hidden;
    background: linear-gradient(135deg, var(--white) 0%, var(--silver-light) 45%, var(--silver-mid) 100%);
  }
  .card-back { left: 50px; top: 90px; }
  .card-front { left: 590px; top: 470px; }
  .card-art { position: absolute; inset: 0; width: 100%; height: 100%; }

  .brand { position: absolute; display: flex; align-items: center; gap: 16px; color: var(--electric-blue); font-weight: 700; }
  .brand-dot { width: 56px; height: 56px; border-radius: 50%; background: var(--electric-blue); flex: none; }
  .brand-name { line-height: 0.95; text-transform: uppercase; }
  .brand-name .line-main { display: block; font-size: 58px; letter-spacing: 2px; }
  .brand-name .line-sub { display: block; font-size: 22px; letter-spacing: 3px; }

  .card-back .brand { left: 70px; top: 100px; }
  .back-contact { position: absolute; left: 110px; top: 232px; font-weight: 700; font-size: 22px; line-height: 1.3; }
  .back-contact .email { color: var(--grey-text); }
  .back-contact .web { color: var(--electric-blue); }

  .card-front .brand { left: 48px; top: 62px; }
  .card-front .brand-name .line-main { font-size: 74px; }
  .card-front .brand-name .line-sub { font-size: 26px; }
  .person-name { position: absolute; left: 80px; top: 218px; color: var(--electric-blue); font-weight: 700; font-size: 26px; letter-spacing: 1px; }
  .phone { position: absolute; left: 80px; top: 274px; color: var(--white); font-weight: 700; font-size: 28px; letter-spacing: 1px; display: flex; align-items: center; gap: 12px; }
  .phone svg { width: 24px; height: 24px; }
  .licence { position: absolute; right: 26px; bottom: 118px; color: var(--white); font-weight: 800; font-size: 26px; letter-spacing: 1px; }
</style>
</head>
<body>

<section class="card card-back" aria-label="Business card, back">
  <svg class="card-art" viewBox="0 0 560 340" aria-hidden="true">
    <circle cx="430" cy="120" r="150" fill="#e6e7ee" opacity="0.7"/>
  </svg>
  <div class="brand">
    <span class="brand-dot"></span>
    <span class="brand-name"><span class="line-main">Korvan</span><span class="line-sub">Electro Services</span></span>
  </div>
  <div class="back-contact">
    <p class="email">info@korvanelectro.com.au</p>
    <p class="web">www.korvanelectro.com.au</p>
  </div>
</section>

<section class="card card-front" aria-label="Business card, front">
  <svg class="card-art" viewBox="0 0 560 340" aria-hidden="true">
    <circle cx="430" cy="150" r="175" fill="#c4c4c8"/>
    <circle cx="430" cy="150" r="130" fill="#d8d8db"/>
    <path d="M420 340 L560 180 L560 340 Z" fill="var(--electric-blue)"/>
    <path d="M0 262 L440 262 L400 322 L0 322 Z" fill="var(--electric-blue)"/>
  </svg>
  <div class="brand">
    <span class="brand-name"><span class="line-main">Korvan</span><span class="line-sub">Electro Services</span></span>
  </div>
  <p class="person-name">DANIEL HARTLEY</p>
  <p class="phone">
    <svg viewBox="0 0 24 24" aria-hidden="true"><path fill="#ffffff" d="M6.6 10.8a15.1 15.1 0 0 0 6.6 6.6l2.2-2.2a1 1 0 0 1 1-.25 11.4 11.4 0 0 0 3.6.57 1 1 0 0 1 1 1V20a1 1 0 0 1-1 1A17 17 0 0 1 3 4a1 1 0 0 1 1-1h3.5a1 1 0 0 1 1 1c0 1.25.2 2.45.57 3.57a1 1 0 0 1-.25 1z"/></svg>
    0412 555 019
  </p>
  <p class="licence">EC20491</p>
</section>

</body>
</html>
```